Gluten Free Bakery Relaunch Ad series

Would like a series of three cohesive ads for use in social media to build buzz leading up to our grand reopening May 1st. Would like to use a single existing product photo as the PRIMARY background in each ad, featuring text along the lines of "gluten free never looked so good," "the wait is over," or something similar as well as the company name "CRUMB: A Harbor Bakery." Feel free to visit www.crumbovenhouse.com, facebook.com/CrumbOvenHouse or @CrumbOvenHouse for more info on the background/feel of the company. Thanks!

Target Market(s)

Gluten free diet, age 20-40, for use on social media

Industry/Entity Type

It Company

Font styles to use
Serif
Sans Serif

Colors
ffffff

Requirements
Must have
• Include reopening date "May 1st", not too feminine
Nice to have
• You are not wedded to the example slogans above. Please feel free to experiment with creative or catchy tag lines.

Big fan of the following fonts, just as an example, not mandatory: Pluto, Gotham, Oxtail

```html
<!DOCTYPE html>
<html lang="en">
<head>
<meta charset="utf-8">
<title>CRUMB: A Harbor Bakery — Reopening Ad Series</title>
<link href="https://fonts.googleapis.com/css2?family=Montserrat:wght@300;400;700&display=swap" rel="stylesheet">
<style>
  :root {
    --white: #ffffff;
    --cream: #f6f1e7;
    --badge-ink: #2b2320;
    --crimson-1: #9b1c22; --crimson-2: #4a0d10;
    --amber-1: #d98a1c;   --amber-2: #3d2410;
    --natural-1: #7a5a48; --natural-2: #1a1412; --natural-3: #b9c0c8;
    --green-1: #1f9a45;   --green-2: #0b3a1a;
    --blue-1: #2a9bd6;    --blue-2: #0c2c44;
    --red-1: #e2242b;     --red-2: #5a0a0d;
  }
  * { margin: 0; padding: 0; box-sizing: border-box; }
  html, body { width: 1200px; height: 811px; overflow: hidden; background: var(--white); }
  body { font-family: "Montserrat", "Helvetica Neue", Arial, sans-serif; }

  .series { position: relative; width: 1200px; height: 811px; }

  .ad {
    position: absolute;
    width: 372px; height: 373px;
    overflow: hidden;
    color: var(--white);
  }
  .ad--r1 { top: 13px; }
  .ad--r2 { top: 426px; }
  .ad--c1 { left: 19px; }
  .ad--c2 { left: 418px; }
  .ad--c3 { left: 809px; }

  .ad__photo { position: absolute; inset: 0; }
  .photo--crimson { background: radial-gradient(ellipse at 40% 45%, var(--crimson-1), var(--crimson-2) 85%); }
  .photo--amber   { background: radial-gradient(ellipse at 40% 45%, var(--amber-1), var(--amber-2) 85%); }
  .photo--natural { background: linear-gradient(180deg, var(--natural-2) 0%, var(--natural-1) 45%, var(--natural-3) 100%); }
  .photo--green   { background: radial-gradient(ellipse at 45% 40%, var(--green-1), var(--green-2) 90%); }
  .photo--blue    { background: radial-gradient(ellipse at 45% 40%, var(--blue-1), var(--blue-2) 90%); }
  .photo--red     { background: radial-gradient(ellipse at 45% 55%, var(--red-1), var(--red-2) 90%); }

  .ad__headline {
    position: absolute; left: 0; right: 0; top: 72px;
    text-align: center;
    text-transform: uppercase;
    font-weight: 300;
    line-height: 1;
  }
  .ad__headline span { display: block; }
  .headline--gf .line-a { font-size: 40px; }
  .headline--gf .line-b { font-size: 33px; }
  .headline--gf .line-c { font-size: 54px; margin-top: 4px; }
  .headline--bold { font-weight: 700; }
  .headline--bold .line-a { font-size: 37px; }
  .headline--bold .line-b { font-size: 33px; }
  .headline--bold .line-c { font-size: 53px; }
  .headline--bold span { text-shadow: 2px 2px 0 rgba(90,20,20,0.8); }

  .headline--flavor { top: 96px; }
  .headline--flavor span { font-size: 35px; line-height: 1.1; }
  .headline--flavor .line-c { font-weight: 700; }

  .ad__date {
    position: absolute; left: 21px; bottom: 22px;
    font-size: 24px; font-weight: 400; line-height: 1.15;
  }

  .ad__badge {
    position: absolute; right: 8px; bottom: 0;
    width: 140px; height: 120px;
  }
  .badge__shape { position: absolute; inset: 0; }
  .badge__name {
    position: absolute; left: 0; right: 0; top: 50px;
    text-align: center;
    font-size: 24px; font-weight: 700; letter-spacing: 2px;
    color: var(--badge-ink);
  }
</style>
</head>
<body>
<main class="series">

  <!-- Row 1: Gluten free -->
  <section class="ad ad--r1 ad--c1">
    <div class="ad__photo photo--crimson" role="img" aria-label="Stacked gluten free sandwich cookies, crimson duotone"></div>
    <h2 class="ad__headline headline--gf"><span class="line-a">Gluten Free</span><span class="line-b">Never Looked</span><span class="line-c">So Good</span></h2>
    <p class="ad__date">Reopening<br>May 1st</p>
    <div class="ad__badge">
      <svg class="badge__shape" viewBox="0 0 140 120" aria-hidden="true"><path d="M0 120 V55 A70 55 0 0 1 140 55 V120 Z" fill="var(--cream)"/></svg>
      <span class="badge__name">CRUMB</span>
    </div>
  </section>

  <section class="ad ad--r1 ad--c2">
    <div class="ad__photo photo--amber" role="img" aria-label="Stacked gluten free sandwich cookies, amber duotone"></div>
    <h2 class="ad__headline headline--gf"><span class="line-a">Gluten Free</span><span class="line-b">Never Looked</span><span class="line-c">So Good</span></h2>
    <p class="ad__date">Reopening<br>May 1st</p>
    <div class="ad__badge">
      <svg class="badge__shape" viewBox="0 0 140 120" aria-hidden="true"><path d="M0 120 V55 A70 55 0 0 1 140 55 V120 Z" fill="var(--cream)"/></svg>
      <span class="badge__name">CRUMB</span>
    </div>
  </section>

  <section class="ad ad--r1 ad--c3">
    <div class="ad__photo photo--natural" role="img" aria-label="Stacked chocolate sandwich cookies with cream filling, natural colour"></div>
    <h2 class="ad__headline headline--gf headline--bold"><span class="line-a">Gluten Free</span><span class="line-b">Never Looked</span><span class="line-c">So Good</span></h2>
    <p class="ad__date">Reopening<br>May 1st</p>
    <div class="ad__badge">
      <svg class="badge__shape" viewBox="0 0 140 120" aria-hidden="true"><path d="M0 120 V55 A70 55 0 0 1 140 55 V120 Z" fill="var(--cream)"/></svg>
      <span class="badge__name">CRUMB</span>
    </div>
  </section>

  <!-- Row 2: Best flavor -->
  <section class="ad ad--r2 ad--c1">
    <div class="ad__photo photo--green" role="img" aria-label="Close-up of chocolate chip cookies, green duotone"></div>
    <h2 class="ad__headline headline--flavor"><span class="line-a">Get Ready For</span><span class="line-b">The Best Flavor</span><span class="line-c">Healthy</span></h2>
    <p class="ad__date">Reopening<br>May 1st</p>
    <div class="ad__badge">
      <svg class="badge__shape" viewBox="0 0 140 120" aria-hidden="true"><path d="M0 120 V55 A70 55 0 0 1 140 55 V120 Z" fill="var(--cream)"/></svg>
      <span class="badge__name">CRUMB</span>
    </div>
  </section>

  <section class="ad ad--r2 ad--c2">
    <div class="ad__photo photo--blue" role="img" aria-label="Close-up of chocolate chip cookies, blue duotone"></div>
    <h2 class="ad__headline headline--flavor"><span class="line-a">Get Ready For</span><span class="line-b">The Best Flavor</span><span class="line-c">Healthy</span></h2>
    <p class="ad__date">Reopening<br>May 1st</p>
    <div class="ad__badge">
      <svg class="badge__shape" viewBox="0 0 140 120" aria-hidden="true"><path d="M0 120 V55 A70 55 0 0 1 140 55 V120 Z" fill="var(--cream)"/></svg>
      <span class="badge__name">CRUMB</span>
    </div>
  </section>

  <section class="ad ad--r2 ad--c3">
    <div class="ad__photo photo--red" role="img" aria-label="Close-up of chocolate chip cookies, red duotone"></div>
    <h2 class="ad__headline headline--flavor"><span class="line-a">Get Ready For</span><span class="line-b">The Best Flavor</span><span class="line-c">Healthy</span></h2>
    <p class="ad__date">Reopening<br>May 1st</p>
    <div class="ad__badge">
      <svg class="badge__shape" viewBox="0 0 140 120" aria-hidden="true"><path d="M0 120 V55 A70 55 0 0 1 140 55 V120 Z" fill="var(--cream)"/></svg>
      <span class="badge__name">CRUMB</span>
    </div>
  </section>

</main>
</body>
</html>
```